KPV Construction we build lodges in Botswana

We need a Design Layout only with Categories where we can update each projects photos.... We have a web address and a host - kpv.construction

```html
<!DOCTYPE html>
<html lang="en">
<head>
<meta charset="utf-8">
<title>KPV Construction</title>
<link href="https://fonts.googleapis.com/css2?family=Montserrat:wght@400;500;600;700;800&family=Open+Sans:wght@400;600;700&display=swap" rel="stylesheet">
<style>
:root{
  --blue:#1e6fd9;
  --blue-dark:#1553a8;
  --navy:#0d2a52;
  --red:#e8141c;
  --ink:#2b2f36;
  --muted:#7b8088;
  --line:#e2e4e8;
  --paper:#ffffff;
  --grey:#f2f3f5;
}
*{box-sizing:border-box;margin:0;padding:0}
html,body{width:1200px;height:2896px;overflow:hidden;background:var(--paper)}
body{font-family:"Open Sans",Arial,sans-serif;color:var(--ink)}
.page{position:relative;width:1200px;height:2896px;overflow:hidden;background:var(--paper)}
.red-rail{position:absolute;left:0;top:60px;width:88px;height:2740px;background:var(--red)}

/* top bar */
.topbar{position:absolute;left:0;top:0;width:1200px;height:60px;background:var(--paper)}
.social{position:absolute;left:680px;top:16px;display:flex;gap:10px}
.social span{width:26px;height:26px;border-radius:50%;border:1.5px solid #9aa0a8;display:block}
.call{position:absolute;right:0;top:0;width:340px;height:60px;background:var(--blue);display:flex;align-items:center;padding-left:22px;gap:14px;color:#fff}
.call svg{width:26px;height:26px}
.call small{display:block;font:600 11px "Montserrat",sans-serif;letter-spacing:1px}
.call strong{display:block;font:700 22px "Montserrat",sans-serif;letter-spacing:.5px}

/* hero */
.hero{position:absolute;left:88px;top:60px;width:1112px;height:672px;background:linear-gradient(180deg,#8fb3d6 0%,#c9d9e6 30%,#6e8aa6 58%,#2a3c52 78%,#1d2d3f 100%)}
.hero-content{position:absolute;left:184px;top:0;width:928px;height:100%}
.hero-brand{position:absolute;left:0;width:100%;top:170px;display:flex;justify-content:center;align-items:center;gap:14px}
.hero-brand i{width:34px;height:34px;background:var(--red);display:block}
.hero-brand span{font:800 34px "Montserrat",sans-serif;color:var(--blue-dark)}
.hero h1{position:absolute;top:314px;left:0;width:100%;text-align:center;font:700 42px "Montserrat",sans-serif;color:#fff;letter-spacing:.5px;white-space:nowrap}
.hero p{position:absolute;top:382px;left:124px;width:680px;text-align:center;font-size:14px;line-height:22px;color:#eef3f8}
.hero-actions{position:absolute;top:474px;left:0;width:100%;display:flex;justify-content:center;gap:24px}
.btn{display:inline-block;font:600 15px "Montserrat",sans-serif;padding:12px 34px;text-decoration:none}
.btn-dark{background:#1a1d22;color:#fff;border:1.5px solid #fff}
.btn-red{background:var(--red);color:#fff}

/* sidebar */
.sidebar{position:absolute;left:32px;top:60px;width:240px;height:672px;background:var(--blue);box-shadow:0 6px 20px rgba(0,0,0,.25)}
.side-brand{height:200px;background:var(--blue-dark);display:flex;flex-direction:column;align-items:center;justify-content:center;gap:12px}
.side-brand i{width:60px;height:60px;background:#fff;display:block}
.side-brand span{font:700 16px "Montserrat",sans-serif;color:#fff}
.side-nav{list-style:none;padding:34px 0 0}
.side-nav li{font:600 13px "Montserrat",sans-serif;color:#fff;padding:0 28px;height:46px;display:flex;align-items:center;justify-content:space-between;border-bottom:1px solid rgba(255,255,255,.18)}
.side-nav li.sub{padding-left:46px;font-weight:500;height:40px}

/* projects */
.section-title{font:700 24px "Montserrat",sans-serif;color:var(--blue-dark);padding-left:16px;border-left:5px solid var(--red);line-height:30px}
.projects-head{position:absolute;left:112px;top:815px;width:1060px;display:flex;justify-content:space-between;align-items:center;border-bottom:1px solid var(--line);padding-bottom:18px}
.filters{display:flex;gap:30px;font:500 16px "Montserrat",sans-serif;color:var(--muted)}
.filters .on{color:var(--ink);border-bottom:2px solid var(--blue);padding-bottom:4px}
.gallery{position:absolute;left:112px;top:900px;display:flex;gap:20px}
.gallery div{width:252px;height:460px}
.g1{background:linear-gradient(160deg,#e9e6e4,#b9b1ab 60%,#8c7f78)}
.g2{background:linear-gradient(180deg,#d8e6f2,#f4f6f8 40%,#cfd6dc)}
.g3{background:linear-gradient(150deg,#5a3a26,#b07a4c 50%,#d9b08a)}
.g4{background:linear-gradient(170deg,#f5f5f3,#d7d8d6 60%,#b5b7b6)}
.pager{position:absolute;right:40px;top:1394px;font:600 13px "Montserrat",sans-serif;color:var(--ink);display:flex;gap:26px}

/* welcome */
.welcome{position:absolute;left:138px;top:1576px;width:500px}
.welcome .eyebrow{font:700 18px "Montserrat",sans-serif;color:var(--ink)}
.welcome h2{font:800 34px "Montserrat",sans-serif;color:var(--blue-dark);margin-top:4px}
.welcome h3{font:600 19px "Montserrat",sans-serif;color:var(--ink);margin-top:22px;padding-bottom:14px;border-bottom:3px solid var(--blue);display:inline-block}
.welcome p{font-size:14px;line-height:24px;color:var(--muted);margin-top:26px;width:490px}
.btn-outline{margin-top:34px;font:700 13px "Montserrat",sans-serif;color:var(--blue-dark);border:2px solid var(--blue-dark);padding:10px 18px;display:inline-block}
.welcome-media{position:absolute;left:710px;top:1582px;width:370px;height:480px}
.welcome-media .frame{position:absolute;left:0;top:0;width:370px;height:420px;border:22px solid var(--blue-dark)}
.welcome-media .photo{position:absolute;left:96px;top:82px;width:310px;height:398px;background:linear-gradient(180deg,#dfe6ee,#c8d2dc 45%,#7d8ea3 75%,#3d4b5e)}

/* banner */
.grey-zone{position:absolute;left:88px;top:2180px;width:1112px;height:716px;background:var(--grey)}
.banner{position:absolute;left:88px;top:2252px;width:1032px;height:136px}
.banner svg{position:absolute;inset:0}
.banner p{position:absolute;left:40px;top:44px;font:500 38px "Montserrat",sans-serif;color:#fff}
.banner p u{text-underline-offset:6px}

/* footer */
.footer{position:absolute;left:128px;top:2440px;width:1000px;display:grid;grid-template-columns:300px 300px 300px;gap:50px}
.footer h4{font:600 20px "Montserrat",sans-serif;color:var(--ink);padding-bottom:14px;border-bottom:1px solid #cfd2d6;margin-bottom:18px}
.footer p{font-size:13px;line-height:21px;color:var(--muted)}
.hours{margin-top:22px;width:260px}
.hours div{display:flex;justify-content:space-between;font-size:12px;color:var(--muted);padding:7px 0;border-bottom:1px solid #dcdfe3}
.hours b{color:var(--ink);font-weight:600}
.links{display:grid;grid-template-columns:1fr 1fr;font-size:13px;line-height:26px;color:var(--muted)}
.lang{position:absolute;left:1000px;top:2808px;width:64px;height:26px;border:1px solid #c4c8cd;background:#fff;font-size:11px;display:flex;align-items:center;justify-content:space-around;color:var(--ink)}
.copyright{position:absolute;left:128px;top:2856px;font-size:12px;color:var(--muted)}
</style>
</head>
<body>
<div class="page">
  <div class="red-rail"></div>

  <header class="topbar">
    <div class="social"><span></span><span></span><span></span><span></span><span></span></div>
    <div class="call">
      <svg viewBox="0 0 24 24" fill="none" stroke="#fff" stroke-width="2"><path d="M5 3h4l2 5-3 2a11 11 0 0 0 6 6l2-3 5 2v4a2 2 0 0 1-2 2A17 17 0 0 1 3 5a2 2 0 0 1 2-2z"/></svg>
      <div><small>CALL US AT</small><strong>1800-555-0199</strong></div>
    </div>
  </header>

  <section class="hero" role="img" aria-label="City skyline at dusk with sunlit clouds over tall buildings">
    <div class="hero-content">
      <div class="hero-brand"><i></i><span>KPV Construction</span></div>
      <h1>WE BUILD BIG THINGS FOR YOU</h1>
      <p>We design and build lodges, homes and commercial buildings across Botswana, delivering quality work on time and within budget for every client we serve.</p>
      <div class="hero-actions"><a class="btn btn-dark">Get Started</a><a class="btn btn-red">Contact Us</a></div>
    </div>
  </section>

  <aside class="sidebar">
    <div class="side-brand"><i></i><span>KPV Construction</span></div>
    <ul class="side-nav">
      <li>HOME</li>
      <li>PROJECTS <span>+</span></li>
      <li class="sub">PROJECT 1</li>
      <li class="sub">PROJECT 2</li>
      <li class="sub">PROJECT 3</li>
      <li>CONTACT</li>
    </ul>
  </aside>

  <div class="projects-head">
    <h2 class="section-title">PROJECTS</h2>
    <nav class="filters"><span class="on">All</span><span>Restaurant</span><span>Buildings</span><span>Apartments</span></nav>
  </div>
  <div class="gallery">
    <div class="g1" role="img" aria-label="Spiral staircase in a white building interior"></div>
    <div class="g2" role="img" aria-label="Modern white apartment facade with balconies"></div>
    <div class="g3" role="img" aria-label="Curved wooden staircase seen from above"></div>
    <div class="g4" role="img" aria-label="White curved architectural interior"></div>
  </div>
  <div class="pager"><span>‹ PREV</span><span>NEXT ›</span></div>

  <section class="welcome">
    <div class="eyebrow">WELCOME TO</div>
    <h2>CONSTRUCTION COMPANY</h2>
    <h3>YEARS OF EXPERIENCE</h3>
    <p>We are a Botswana based building team with years of hands-on experience in lodges, homes and commercial spaces. From the first sketch to the final handover we manage every step, working with local suppliers and skilled crews. Our projects are built to last in demanding climates and remote locations, and we keep clients informed through clear planning, honest pricing and regular site updates. Every build reflects care, safety and quality.</p>
    <span class="btn-outline">KNOW MORE</span>
  </section>
  <div class="welcome-media">
    <div class="frame"></div>
    <div class="photo" role="img" aria-label="Construction team in hard hats in front of office buildings"></div>
  </div>

  <div class="grey-zone"></div>
  <div class="banner">
    <svg viewBox="0 0 1032 136" width="1032" height="136" preserveAspectRatio="none"><polygon points="0,0 1032,0 960,136 0,136" fill="#1e6fd9"/></svg>
    <p>Believe Professionals. <u>Contact Us</u></p>
  </div>

  <footer class="footer">
    <div>
      <h4>ABOUT COMPANY</h4>
      <p>We are an award winning construction company focused on user driven outcomes. We strive to create meaningful connections for users through considered strategy and innovation in the building space.</p>
    </div>
    <div>
      <h4>BUSINESS HOURS</h4>
      <p>We are happy to meet you during our working hours. Please make an appointment.</p>
      <div class="hours">
        <div><span>Monday-Friday:</span><b>9am to 5pm</b></div>
        <div><span>Saturday:</span><b>9am to 2pm</b></div>
        <div><span>Sunday:</span><b>Closed</b></div>
      </div>
    </div>
    <div>
      <h4>HELPFUL LINKS</h4>
      <div class="links">
        <span>Our services</span><span>Disclaimer</span>
        <span>Showcase</span><span>Privacy Policy</span>
        <span>Affiliates</span><span></span>
      </div>
    </div>
  </footer>
  <div class="lang"><span>EN</span><span>▾</span></div>
  <div class="copyright">© 2016 - 2018 KPV Construction, All rights reserved.</div>
</div>
</body>
</html>
```